Clinvora Franchise LLC Informational Catalogue/Flipbook

We are seeking a professional, yet inviting informational catalogue/flipbook on owning a medical waste franchise with Clinvora Franchise LLC. Our vision is to print this catalogue in color, landscape orientation, spiral-bound, and about 6in x 9in in size.
For branding continuity, please refer to our website: www.clinvora-example.com.
Attached please find the text copy, organized by page, as well as a .zip folder containing photos that can be used throughout the catalogue. Not all of the photos have to be used, so chose at your own discretion.
Look and feel
Each slider illustrates characteristics of the customer's brand and the style your logo design should communicate.

```html
<!DOCTYPE html>
<html lang="en">
<head>
<meta charset="utf-8">
<title>Clinvora Franchise Catalogue – Pages 6 to 9</title>
<link rel="stylesheet" href="https://fonts.googleapis.com/css2?family=Fira+Sans+Condensed:wght@400;500&family=Roboto:wght@400;500&family=Open+Sans:wght@800&display=swap">
<style>
  :root {
    --board: #bcbcbc;
    --ink: #1c1c1c;
    --brand-red: #d42a2e;
    --row-tint: #f7e0dc;
    --page-white: #ffffff;
    --tick-green: #3aa03a;
    --cream: #fff4ec;
  }
  * { margin: 0; padding: 0; box-sizing: border-box; }
  html, body { width: 1200px; height: 848px; overflow: hidden; background: var(--board); }
  .board { position: relative; width: 1200px; height: 848px; }

  .page-label {
    position: absolute; width: 448px; text-align: center;
    font: 800 18px/1 "Open Sans", sans-serif; color: #111;
  }

  .spread {
    position: absolute; left: 152px; width: 896px; height: 299px;
    display: flex; box-shadow: 4px 5px 6px rgba(0,0,0,0.35);
  }
  .spread--top { top: 75px; }
  .spread--bottom { top: 472px; }
  .page { position: relative; width: 448px; height: 299px; overflow: hidden; }

  .page-title {
    position: absolute; font: 500 15px/1 "Fira Sans Condensed", sans-serif; color: var(--brand-red);
    white-space: nowrap;
  }

  /* Page 6: investment */
  .investment { background: var(--page-white); }
  .investment .page-title { left: 39px; top: 11px; }
  .investment-summary {
    position: absolute; left: 39px; top: 27px;
    font: 400 6.8px/1 "Fira Sans Condensed", sans-serif; color: #000;
  }
  .cost-table {
    position: absolute; left: 39px; top: 39px; width: 371px;
    border: 1.5px solid var(--brand-red); border-collapse: collapse;
    font-family: "Roboto", sans-serif; color: #000;
  }
  .cost-table th, .cost-table td { text-align: left; vertical-align: top; font-weight: 400; }
  .cost-table th {
    background: var(--brand-red); color: #fff; font-size: 6.6px;
    height: 12.5px; padding: 2px 4px 0;
  }
  .cost-table td {
    font-size: 4.9px; height: 11.7px; padding: 3.2px 2px 0; line-height: 1;
    background: var(--page-white);
  }
  .cost-table td:first-child { width: 88px; border-right: 1px solid var(--brand-red); }
  .cost-table th:first-child { border-right: 1px solid #fff; }
  .cost-table tbody tr:nth-child(odd) td { background: var(--row-tint); }
  .cost-table .fee-row td { height: 57px; padding-top: 3px; }
  .fee-list { list-style: none; line-height: 5.85px; font-size: 4.6px; }
  .fee-list li { padding-left: 4px; text-indent: -4px; }
  .fee-list li::before { content: "• "; }
  .cost-table tfoot td {
    background: var(--brand-red); color: #fff; font-size: 6.6px; height: 13.6px; padding: 3px 6px 0;
  }
  .cost-table tfoot td:first-child { border-right: 1px solid #fff; }

  /* Page 7: revenue */
  .revenue {
    background:
      radial-gradient(ellipse 60% 80% at 88% 62%, rgba(176,31,39,0.55) 0%, rgba(176,31,39,0) 70%),
      linear-gradient(90deg, #e97679 0%, #e05355 45%, #d6302f 100%);
  }
  .revenue .page-title { left: 30px; top: 51px; }
  .revenue-list { position: absolute; left: 30px; top: 78px; list-style: none; }
  .revenue-list li {
    display: flex; align-items: center; gap: 7px; height: 22.5px;
    font: 400 9.4px/1 "Fira Sans Condensed", sans-serif; color: var(--cream); white-space: nowrap;
  }
  .tick { width: 11px; height: 11px; flex: none; }

  /* Page 8: training */
  .training { background: linear-gradient(100deg, #e8e8e8 0%, #dedede 100%); }
  .training-photo {
    position: absolute; right: 0; top: 0; width: 230px; height: 299px;
    background:
      radial-gradient(ellipse 38% 30% at 62% 30%, #c9a58f 0%, rgba(201,165,143,0) 100%),
      radial-gradient(ellipse 60% 45% at 70% 95%, #6fbfae 0%, rgba(111,191,174,0) 100%),
      linear-gradient(90deg, rgba(222,222,222,0) 0%, #d3d6d5 35%, #c4cfcc 100%);
  }
  .training .page-title { left: 30px; top: 51px; }
  .training-list { position: absolute; left: 30px; top: 79px; list-style: none; }
  .training-list li {
    height: 22.5px; font: 400 9px/1 "Fira Sans Condensed", sans-serif; color: var(--ink); white-space: nowrap;
  }

  /* Page 9: shredding */
  .shredding { background: var(--page-white); }
  .shredding .page-title { left: 30px; top: 51px; }
  .shredding-copy {
    position: absolute; left: 30px; width: 290px;
    font: 400 7px/10.3px "Fira Sans Condensed", sans-serif; color: var(--ink);
  }
  .shredding-copy--one { top: 81px; }
  .shredding-copy--two { top: 111px; }
  .shredding-copy--three { top: 146px; }
  .service-name {
    position: absolute; left: 30px; top: 218px; display: flex; align-items: center; gap: 8px;
    font: 500 24px/1 "Fira Sans Condensed", sans-serif; color: #111;
  }
  .service-name .mark { width: 26px; height: 26px; background: #111; }
</style>
</head>
<body>
<div class="board">
  <div class="page-label" style="left:152px; top:42px;">PAGE 6</div>
  <div class="page-label" style="left:600px; top:42px;">PAGE 7</div>
  <div class="page-label" style="left:152px; top:438px;">PAGE 8</div>
  <div class="page-label" style="left:600px; top:438px;">PAGE 9</div>

  <div class="spread spread--top">
    <section class="page investment">
      <h2 class="page-title">The Investment</h2>
      <p class="investment-summary">Liquid Capital Requirement: $101,535 to $141,985.&nbsp; Initial Investment: $50,000</p>
      <table class="cost-table">
        <thead><tr><th>Expenses:</th><th>Amount:</th></tr></thead>
        <tbody>
          <tr class="fee-row"><td>Initial Franchise Fee</td><td>
            <ul class="fee-list">
              <li>$50,000 - Includes the following:</li>
              <li>Territory Size: 0 – 500,000</li>
              <li>Due diligence review</li>
              <li>A dedicated Environmental, Health and Safety (EHS) consultant to provide assistance in the obtaining of licensing, in locating and negotiating the processing and transfer station drop-off location, and training in the handling of medical waste</li>
              <li>Training and all training materials</li>
              <li>The creation of distinct, geographically-specific web pages on Clinvora Franchise LLC websites</li>
              <li>$5,000 worth of supplies, including boxes, red bags, and sharps containers</li>
              <li>Direct phone line through CallNest/VOIP service</li>
            </ul></td></tr>
          <tr><td>Business Permit &amp; License</td><td>$1,200 - $8,500</td></tr>
          <tr><td>Office Lease (Deposit)</td><td>$2,500 - $4,000</td></tr>
          <tr><td>Vehicle Lease</td><td>$5,000 - $8,000</td></tr>
          <tr><td>Initial Inventory</td><td>FREE - Included in the Franchise Fee</td></tr>
          <tr><td>Computer Systems &amp; Setup</td><td>$1,500 - $3,000</td></tr>
          <tr><td>Uniforms</td><td>$100 - $500</td></tr>
          <tr><td>Office Equipment &amp; Supplies</td><td>$585 - $2,185</td></tr>
          <tr><td>Professional Fees</td><td>$2,500 - $5,500</td></tr>
          <tr><td>Advertising &amp; Marketing</td><td>$7,150 - $10,500</td></tr>
          <tr><td>Insurance</td><td>$3,650 - $5,300</td></tr>
          <tr><td>Additional Inventory &amp; Supplies</td><td>$250 - $1,000</td></tr>
          <tr><td>Equipment &amp; Tools</td><td>$100 - $500</td></tr>
          <tr><td>Travel Expenses</td><td>$2,000 - $3,000</td></tr>
          <tr><td>Operation Expenses (3 months)</td><td>$25,000 - $40,000</td></tr>
        </tbody>
        <tfoot><tr><td>TOTAL</td><td>$101,535 - $141,985</td></tr></tfoot>
      </table>
    </section>

    <section class="page revenue">
      <h2 class="page-title">How We Build Revenue</h2>
      <ul class="revenue-list">
        <li><svg class="tick" viewBox="0 0 11 11"><rect width="11" height="11" fill="#fff"/><path d="M2 5.8 4.3 8.5 9.5 1.8" fill="none" stroke="var(--tick-green)" stroke-width="1.8"/></svg>Advanced SEO, Marketing &amp; Sales Engine</li>
        <li><svg class="tick" viewBox="0 0 11 11"><rect width="11" height="11" fill="#fff"/><path d="M2 5.8 4.3 8.5 9.5 1.8" fill="none" stroke="var(--tick-green)" stroke-width="1.8"/></svg>Diverse Revenue Streams</li>
        <li><svg class="tick" viewBox="0 0 11 11"><rect width="11" height="11" fill="#fff"/><path d="M2 5.8 4.3 8.5 9.5 1.8" fill="none" stroke="var(--tick-green)" stroke-width="1.8"/></svg>Outstanding Customer Service</li>
        <li><svg class="tick" viewBox="0 0 11 11"><rect width="11" height="11" fill="#fff"/><path d="M2 5.8 4.3 8.5 9.5 1.8" fill="none" stroke="var(--tick-green)" stroke-width="1.8"/></svg>Strategic Relationships &amp; Partnerships</li>
      </ul>
    </section>
  </div>

  <div class="spread spread--bottom">
    <section class="page training">
      <div class="training-photo" role="img" aria-label="Photo of a smiling support agent in teal scrubs wearing a headset, on a light grey background"></div>
      <h2 class="page-title">Training &amp; Coaching You Will Receive</h2>
      <ul class="training-list">
        <li>A robust training manual</li>
        <li>5 days of on-site training at our Maple Ridge, NY or Harbor Point, CT locations</li>
        <li>2 days of on-site training at your location</li>
        <li>Complimentary registration for up to 3 team members at the annual franchise conference</li>
        <li>Bimonthly franchise VidLink meetups</li>
        <li>Quarterly franchise review conference calls</li>
        <li>Ongoing support and coaching</li>
      </ul>
    </section>

    <section class="page shredding">
      <h2 class="page-title">SwiftShred</h2>
      <p class="shredding-copy shredding-copy--one">As a Clinvora Franchise owner, you’ll also have the opportunity to expand into the document destruction business through SwiftShred, the document destruction arm of our business.</p>
      <p class="shredding-copy shredding-copy--two">SwiftShred offers mobile and off-site document and media destruction services for both residential and business clients.</p>
      <p class="shredding-copy shredding-copy--three">These additional service offerings allow Franchise owners to increase and diversify their revenue streams, while offering their clients a more comprehensive service package.</p>
      <div class="service-name"><span class="mark"></span>SwiftShred</div>
    </section>
  </div>
</div>
</body>
</html>
```